Need help refining Solkvartsgillet

Hi We need help with the refining of overall design and details of our homepage design Solkvartsgillet. See attached files.

Attached files:
homepage.psd - file you can use to work from.
homepage.png – quick notes on thoughts of the design
logo.psd (smart object) – The logo should be in gold.
social media elements.png - what type of data that needs design in the feed

What we need:
Something is missing with the overall design as well as detailed design for our social media feed. We don’t know what and hope you can solve this for us.

The homepage:
Our main page include a selfloading blogfeed combined with Pageloop- and Instagramfeed.

Fonts:
So far I´ve used Roboto regular, and Georgia, but feel free to use other fonts if you find better suited

Among others, we need a better detailed design that works better with the overall design.

Se attached sample image (social_mediafeed.png) what types of data we get from Pageloop in our feed. Feel free to redesign the elements of this data.

Headerlinks:
Even though we only have one page, there should be place for links to other pages as well which will load below the header.

Social media follow: Place for social media follow links/icons/buttons in style with rest of the design. Maybe at top grey border? We use Glimtora and Pageloop in style with rest of the design.

Colors:
The logo should be in gold, and use of "goldish" colors troughout the page.
Also blue elements troughout the page

Logo in gold/goldish color
Blue elements # 13416c (or similar color that works well in the design)

Target Market(s)

Wellness, fitness, spa and food, Exclusive

Number of Pages Required

1 page

Font styles to use
Serif
Sans Serif
Script
Other font styles liked:
• Roboto, Georgia

Requirements
Must have
• Better overall design that feel harmonic.
• Better design of blog and social media feeds (se all attached images)
• Nice clean design, easy on the eye
• Colors on theme: Gold + blue

```html
<!DOCTYPE html>
<html lang="sv">
<head>
<meta charset="utf-8">
<title>Solkvartsgillet – Hem</title>
<link href="https://fonts.googleapis.com/css2?family=Roboto:wght@300;400;500;700&family=Oswald:wght@300;400&family=Playfair+Display:wght@400&display=swap" rel="stylesheet">
<style>
:root{
  --blue:#13416c;
  --blue-dark:#0f3456;
  --gold:#c9a24d;
  --gold-light:#dcc07f;
  --text:#4a4a4a;
  --muted:#8a8a8a;
  --line:#e3e3e3;
  --section-grey:#eeeeee;
  --white:#ffffff;
  --red:#d34836;
  --sky:#2aa3d8;
}
*{box-sizing:border-box;margin:0;padding:0}
html,body{width:1200px;height:3727px;overflow:hidden}
body{position:relative;background:var(--white);font-family:"Roboto",Arial,sans-serif;color:var(--text);font-size:14px}
.abs{position:absolute}
a{color:inherit;text-decoration:none}

/* top bar */
.member-bar{top:0;left:832px;display:flex;gap:6px}
.member-bar .btn{height:32px;display:flex;align-items:center;gap:10px;padding:0 14px;font-size:13px;color:var(--white)}
.member-bar .join{background:var(--gold);width:122px}
.member-bar .login{background:var(--blue);width:138px}
.member-bar svg{width:16px;height:16px}

/* nav */
.nav{top:88px;font-size:14px;font-weight:500;color:var(--blue);letter-spacing:.3px;display:flex;justify-content:space-between}
.nav-left{left:99px;width:389px}
.nav-right{left:712px;width:386px}
.nav-rule{height:4px;border-top:2px solid var(--blue);border-bottom:1px solid var(--blue)}
.nav-rule.left{top:110px;left:99px;width:389px}
.nav-rule.right{top:110px;left:712px;width:386px}
.logo{top:18px;left:498px;width:204px;text-align:center;color:var(--gold)}
.logo .crest{width:64px;height:64px;border-radius:50%;background:var(--gold);margin:0 auto 10px}
.logo .name{font-family:"Oswald",Arial,sans-serif;font-weight:400;font-size:22px;letter-spacing:1.5px}
.dropdown{top:124px;left:919px;width:174px;background:var(--white);box-shadow:0 2px 6px rgba(0,0,0,.15);z-index:5}
.dropdown li{list-style:none;font-size:11px;padding:0 14px;height:40px;line-height:40px;color:var(--muted);border-bottom:1px solid var(--line)}
.dropdown li.active{background:var(--gold);color:var(--white);font-weight:500}

/* hero */
.hero{top:166px;left:0;width:1200px;height:554px;background:linear-gradient(180deg,#a9c2c0 0%,#d9ddd0 45%,#c8c4ae 62%,#9ca394 80%,#8b8f7f 100%)}
.hero-box{top:166px;left:352px;width:496px;height:190px;margin-top:168px;background:rgba(255,255,255,.55);text-align:center;padding-top:22px}
.hero-box h1{font-family:"Playfair Display",Georgia,serif;font-weight:400;font-size:50px;color:var(--blue);line-height:1}
.hero-box .flourish{width:180px;height:12px;margin:8px auto 10px}
.hero-box p{font-size:15px;color:var(--text)}
.btn-outline{display:inline-block;border:2px solid var(--blue);color:var(--blue);font-size:13px;font-weight:500;padding:0 16px;height:34px;line-height:30px;background:var(--white)}
.hero-box .btn-outline{margin-top:18px}
.hero-arrow{top:422px;width:50px;height:50px;border-radius:50%;background:rgba(60,60,60,.75);display:flex;align-items:center;justify-content:center}
.hero-arrow svg{width:20px;height:20px}

/* offers */
.offers{top:720px;left:0;width:1200px;height:629px;background:var(--section-grey)}
.section-title{top:784px;left:0;width:1200px;text-align:center;font-family:"Oswald",Arial,sans-serif;font-weight:400;font-size:40px;letter-spacing:1px;color:var(--blue)}
.section-title span{color:var(--gold)}
.section-title .flourish{display:block;width:220px;height:14px;margin:4px auto 0}
.offer-card{top:894px;width:318px;height:398px;background:var(--white);box-shadow:0 1px 4px rgba(0,0,0,.12)}
.offer-card .photo{position:relative;height:236px;background:linear-gradient(180deg,#5b3e7c 0%,#9a5b86 35%,#d48a6c 62%,#3f3a5a 80%,#2b2c40 100%)}
.offer-card .photo .overlay-title{position:absolute;top:22px;left:18px;font-size:22px;color:var(--white)}
.offer-card .photo .overlay-sub{position:absolute;top:120px;left:18px;font-size:14px;color:var(--white)}
.offer-card .badge{position:absolute;left:0;bottom:0;width:84px;height:84px;background:var(--gold);border-top-right-radius:84px;color:var(--white);padding:22px 0 0 6px;line-height:1}
.offer-card .badge b{font-size:28px;font-weight:500;display:block}
.offer-card .badge small{font-size:12px}
.offer-card .body{padding:22px 18px}
.offer-card h3{font-size:14px;font-weight:700;color:var(--gold);letter-spacing:.3px}
.offer-card p{font-size:14px;margin-top:12px}
.offer-card .btn-outline{margin-top:24px;height:32px;line-height:28px;font-size:12px}

/* blog */
.post{left:99px;width:999px}
.post-side{position:absolute;left:0;top:0;width:232px}
.post-title{font-family:"Playfair Display",Georgia,serif;font-size:29px;line-height:1.2;color:var(--blue);font-weight:400}
.post-title-rule{width:58px;height:2px;background:var(--gold);margin:22px 0 24px}
.meta{font-size:11px;display:grid;grid-template-columns:84px 1fr;row-gap:10px;color:var(--text)}
.meta dt{font-weight:700;color:var(--blue-dark)}
.post-actions{position:absolute;left:0;width:232px;border-top:1px solid var(--line);border-bottom:1px solid var(--line);height:40px;display:flex;align-items:center;gap:16px;font-size:11px;color:var(--text)}
.post-actions span{display:flex;align-items:center;gap:8px}
.icon-dot{width:18px;height:18px;border-radius:50%;background:var(--gold);display:inline-flex;align-items:center;justify-content:center}
.icon-dot svg{width:10px;height:10px}
.post-photo{position:absolute;left:259px;top:0;width:740px}
.post-excerpt{position:absolute;left:259px;width:740px;font-size:13px;line-height:1.6}
.post .btn-outline{position:absolute;left:259px;height:32px;line-height:28px;font-size:12px;padding:0 20px}
.divider{left:99px;width:999px;height:1px;background:var(--line)}

/* social */
.feed{top:2596px;width:488px;height:807px}
.feed-head{position:relative;height:30px}
.feed-head .rule{position:absolute;top:4px;left:0;right:0;height:3px;background:var(--blue)}
.feed-head .tab{position:absolute;left:50%;transform:translateX(-50%);top:0;height:22px;padding:0 22px;background:var(--blue);color:var(--white);font-family:"Oswald",Arial,sans-serif;font-size:15px;display:flex;align-items:center;gap:8px}
.feed-head .tab i{width:11px;height:11px;background:var(--white);display:block}
.feed-card{border:1px solid var(--line);border-top:none;margin-top:-8px;padding:30px 30px 0;height:720px}
.feed-author{display:flex;align-items:center;gap:14px;font-size:11px;color:var(--text)}
.feed-author .avatar{width:40px;height:40px;border-radius:50%;background:var(--blue)}
.feed-author b{color:var(--blue);font-weight:700}
.feed-author .stat{display:flex;align-items:center;gap:5px}
.feed-author svg{width:11px;height:11px}
.feed-text{font-size:12px;line-height:1.55;margin-top:22px;height:118px}
.feed-text .tags{color:var(--sky)}
.feed-media{border:1px solid var(--line)}
.feed-media .photo{height:418px}
.feed-media .caption{padding:12px 18px;height:62px}
.feed-media .caption strong{font-family:"Playfair Display",Georgia,serif;font-weight:400;font-size:16px;color:var(--text);display:block}
.feed-media .caption small{font-size:10px;color:var(--muted);letter-spacing:.5px}
.share{position:absolute;bottom:0;left:0;right:0;height:40px;border:1px solid var(--line);border-top:none;display:flex;align-items:center;gap:8px;padding:0 18px;font-size:11px}
.share .c{width:22px;height:22px;border-radius:50%}

/* footer */
.footer{top:3465px;left:0;width:1200px;height:236px;background:var(--blue);color:#c9d4e0}
.footer h4{font-size:13px;font-weight:700;color:var(--white);letter-spacing:.4px;margin-bottom:16px}
.footer .col{position:absolute;top:32px;font-size:12px;line-height:1.5}
.footer .links li{list-style:none;line-height:1.75}
.footer .follow{display:grid;grid-template-columns:repeat(3,30px);gap:8px}
.footer .follow span{width:30px;height:30px;border-radius:50%;border:2px solid #c9d4e0;display:block}
.footer .newsletter form{display:flex;margin-top:14px}
.footer input{width:318px;height:32px;border:none;padding:0 10px;font-family:inherit;font-size:12px}
.footer button{width:80px;height:32px;border:none;background:var(--gold);color:var(--white);font-family:inherit;font-weight:700;font-size:12px}
.copyright{top:3701px;left:0;width:1200px;height:26px;background:var(--blue-dark);color:#c9d4e0;font-size:11px;line-height:26px;padding-left:99px}
</style>
</head>
<body>

<!-- member bar -->
<div class="abs member-bar">
  <a class="btn join" href="#"><svg viewBox="0 0 16 16" fill="none" stroke="#fff" stroke-width="1.6"><path d="M3 13l1-4 7-7 3 3-7 7z"/></svg>Bli medlem</a>
  <a class="btn login" href="#"><svg viewBox="0 0 16 16" fill="none" stroke="#fff" stroke-width="1.6"><circle cx="8" cy="5" r="3"/><path d="M2 15c0-4 3-5 6-5s6 1 6 5"/></svg>Medlemslogin</a>
</div>

<!-- navigation -->
<nav class="abs nav nav-left"><a href="#">HEM</a><a href="#">GILLESRESOR</a><a href="#">INSPIRATION</a></nav>
<div class="abs nav-rule left"></div>
<div class="abs logo"><div class="crest"></div><div class="name">SOLKVARTSGILLET</div></div>
<nav class="abs nav nav-right"><a href="#">MEDLEMSERBJUDANDEN</a><a href="#">OM</a><a href="#">INSPIRATION</a></nav>
<div class="abs nav-rule right"></div>
<ul class="abs dropdown">
  <li class="active">SOLKVARTSGILLET</li>
  <li>GILLESBILJETTER</li>
  <li>RESOR</li>
</ul>

<!-- hero -->
<div class="abs hero" role="img" aria-label="Kvinna med armarna upplyfta mot himlen vid ett lugnt hav"></div>
<div class="abs hero-box">
  <h1>Featured</h1>
  <svg class="flourish" viewBox="0 0 180 12"><line x1="0" y1="6" x2="78" y2="6" stroke="#c9a24d"/><circle cx="90" cy="6" r="4" fill="#c9a24d"/><line x1="102" y1="6" x2="180" y2="6" stroke="#c9a24d"/></svg>
  <p>liten beskrivning av post</p>
  <a class="btn-outline" href="#">LÄS MER</a>
</div>
<div class="abs hero-arrow" style="left:16px"><svg viewBox="0 0 20 20" fill="none" stroke="#fff" stroke-width="2.5"><path d="M13 3l-7 7 7 7"/></svg></div>
<div class="abs hero-arrow" style="left:1134px"><svg viewBox="0 0 20 20" fill="none" stroke="#fff" stroke-width="2.5"><path d="M7 3l7 7-7 7"/></svg></div>

<!-- member offers -->
<section class="abs offers"></section>
<h2 class="abs section-title">SOLKVARTSGILLETS <span>MEDLEMSERBJUDANDEN</span>
  <svg class="flourish" viewBox="0 0 220 14"><line x1="0" y1="7" x2="96" y2="7" stroke="#c9a24d"/><circle cx="110" cy="7" r="5" fill="none" stroke="#c9a24d"/><line x1="124" y1="7" x2="220" y2="7" stroke="#c9a24d"/></svg>
</h2>

<article class="abs offer-card" style="left:99px">
  <div class="photo" role="img" aria-label="Kuststad i solnedgång med lila himmel">
    <span class="overlay-title">Ljusa Dagar AB</span><span class="overlay-sub">Medelhavsvy</span>
    <div class="badge"><b>30%</b><small>Rabatt!</small></div>
  </div>
  <div class="body"><h3>LJUSA DAGAR AB</h3><p>En kort rubrik på erbjudandet</p><a class="btn-outline" href="#">LÄS MER</a></div>
</article>
<article class="abs offer-card" style="left:441px">
  <div class="photo" role="img" aria-label="Kuststad i solnedgång med lila himmel">
    <span class="overlay-title">Ljusa Dagar AB</span><span class="overlay-sub">Medelhavsvy</span>
    <div class="badge"><b>30%</b><small>Rabatt!</small></div>
  </div>
  <div class="body"><h3>LJUSA DAGAR AB</h3><p>En kort rubrik på erbjudandet</p><a class="btn-outline" href="#">LÄS MER</a></div>
</article>
<article class="abs offer-card" style="left:782px">
  <div class="photo" role="img" aria-label="Kuststad i solnedgång med lila himmel">
    <span class="overlay-title">Ljusa Dagar AB</span><span class="overlay-sub">Medelhavsvy</span>
    <div class="badge"><b>30%</b><small>Rabatt!</small></div>
  </div>
  <div class="body"><h3>LJUSA DAGAR AB</h3><p>En kort rubrik på erbjudandet</p><a class="btn-outline" href="#">LÄS MER</a></div>
</article>

<!-- blog post 1 -->
<article class="abs post" style="top:1396px;height:530px">
  <div class="post-side">
    <h2 class="post-title">En trevlig rubrik på ditt blogginlägg</h2>
    <div class="post-title-rule"></div>
    <dl class="meta">
      <dt>POSTED ON</dt><dd>22 OKTOBER, 2016</dd>
      <dt>AV</dt><dd>SOLKVARTSGILLET</dd>
      <dt>COMMENTS</dt><dd>0</dd>
      <dt></dt><dd>SPA, LIVSNJUTNING, YOGA</dd>
    </dl>
  </div>
  <div class="post-actions" style="top:342px">
    <span><i class="icon-dot"><svg viewBox="0 0 10 10" fill="#fff"><circle cx="2" cy="5" r="1.6"/><circle cx="8" cy="2" r="1.6"/><circle cx="8" cy="8" r="1.6"/></svg></i>DELA</span>
    <span><i class="icon-dot"><svg viewBox="0 0 10 10" fill="#fff"><path d="M1 1h8v6H4l-3 2z"/></svg></i>KOMMENTERA</span>
  </div>
  <div class="post-photo" role="img" aria-label="Kvinna i yogaposition på en brygga vid havet i solnedgång" style="height:381px;background:linear-gradient(180deg,#5a7fa8 0%,#9bb2c9 40%,#e9c27e 62%,#7e8fa3 78%,#8b7a66 100%)"></div>
  <p class="post-excerpt" style="top:397px">ed dui consectetur, eleifend nibh et, ultricies justo. Vivamus luctus elit ac lacus placerat laoreet vel at lacus. Sed a molestie ex. Vestibulum ac varius libero. Fusce sollicitudin non tellus lacinia molestie. Sed rhoncus dui a sem accumsan, nec scelerisque augue suscipit. Aliquam eget justo odio. Maecenas in molestie tortor, eu tristique ligula. Suspendisse vulputate urna ut elit iaculi varius.</p>
  <a class="btn-outline" href="#" style="top:497px">LÄS MER</a>
</article>
<div class="abs divider" style="top:1957px"></div>

<!-- blog post 2 -->
<article class="abs post" style="top:1992px;height:530px">
  <div class="post-side">
    <h2 class="post-title">En trevlig rubrik på ditt blogginlägg</h2>
    <div class="post-title-rule"></div>
    <dl class="meta">
      <dt>POSTED ON</dt><dd>22 OKTOBER, 2016</dd>
      <dt>AV</dt><dd>SOLKVARTSGILLET</dd>
      <dt>COMMENTS</dt><dd>0</dd>
      <dt></dt><dd>SPA, LIVSNJUTNING, YOGA</dd>
    </dl>
  </div>
  <div class="post-actions" style="top:342px">
    <span><i class="icon-dot"><svg viewBox="0 0 10 10" fill="#fff"><circle cx="2" cy="5" r="1.6"/><circle cx="8" cy="2" r="1.6"/><circle cx="8" cy="8" r="1.6"/></svg></i>DELA</span>
    <span><i class="icon-dot"><svg viewBox="0 0 10 10" fill="#fff"><path d="M1 1h8v6H4l-3 2z"/></svg></i>KOMMENTERA</span>
  </div>
  <div class="post-photo" role="img" aria-label="Händer i meditationsposition i varmt solnedgångsljus" style="height:378px;background:linear-gradient(135deg,#f4d37a 0%,#f0b357 35%,#d9824d 60%,#8e5a3f 100%)"></div>
  <p class="post-excerpt" style="top:398px">ed dui consectetur, eleifend nibh et, ultricies justo. Vivamus luctus elit ac lacus placerat laoreet vel at lacus. Sed a molestie ex. Vestibulum ac varius libero. Fusce sollicitudin non tellus lacinia molestie. Sed rhoncus dui a sem accumsan, nec scelerisque augue suscipit. Aliquam eget justo odio. Maecenas in molestie tortor, eu tristique ligula. Suspendisse vulputate urna ut elit iaculi varius.</p>
  <a class="btn-outline" href="#" style="top:498px">LÄS MER</a>
</article>
<div class="abs divider" style="top:2554px"></div>

<!-- social feeds -->
<section class="abs feed" style="left:99px">
  <div class="feed-head"><div class="rule"></div><div class="tab"><i></i>Pageloop</div></div>
  <div class="feed-card">
    <div class="feed-author"><span class="avatar"></span><b>Solkvartsgillet</b>
      <span class="stat"><svg viewBox="0 0 11 11" fill="#4a4a4a"><rect x="1" y="2" width="9" height="8"/></svg>23 oktober 19:21</span>
      <span class="stat"><svg viewBox="0 0 11 11" fill="#4a4a4a"><path d="M1 5h2v5H1zM4 5l3-4 1 1-1 3h3v5H4z"/></svg>5</span>
      <span class="stat"><svg viewBox="0 0 11 11" fill="#4a4a4a"><path d="M1 1h9v6H4l-3 3z"/></svg>1 kommentarer</span>
    </div>
    <p class="feed-text">Boosta det friska!<br>Skiva ingefära och citron och häll hett vatten över. Detta är en fantastisk dryck att börja dagen med. Citronen säga ha renande egenskaper och det syns ofta på huden. Ingefära känns extra bra nu i förkylningstider. Denna välgörande dryck är full av antioxidanter som stärker kroppen och ger massor av energi. En god morgonvana för en toppendag.</p>
    <div class="feed-media">
      <div class="photo" role="img" aria-label="Två glas med citron- och ingefärsdryck på en brygga vid en hamn" style="background:linear-gradient(180deg,#c9d3dc 0%,#9fb0bf 35%,#7d8b8f 55%,#c8a56a 75%,#8a6d4a 100%)"></div>
      <div class="caption"><strong>Timeline Photos</strong><small>PAGELOOP.COM</small></div>
    </div>
  </div>
  <div class="share">Dela på <span class="c" style="background:var(--blue)"></span><span class="c" style="background:var(--red)"></span><span class="c" style="background:var(--blue)"></span><span class="c" style="background:var(--sky)"></span></div>
</section>

<section class="abs feed" style="left:611px">
  <div class="feed-head"><div class="rule"></div><div class="tab"><i></i>Glimtora</div></div>
  <div class="feed-card">
    <div class="feed-author"><span class="avatar"></span><b>Solkvartsgillet</b>
      <span class="stat"><svg viewBox="0 0 11 11" fill="#4a4a4a"><rect x="1" y="2" width="9" height="8"/></svg>28 oktober 10:29</span>
      <span class="stat"><svg viewBox="0 0 11 11" fill="#4a4a4a"><path d="M1 5h2v5H1zM4 5l3-4 1 1-1 3h3v5H4z"/></svg>5</span>
      <span class="stat"><svg viewBox="0 0 11 11" fill="#4a4a4a"><path d="M1 1h9v6H4l-3 3z"/></svg>1 kommentarer</span>
    </div>
    <p class="feed-text">Ni vet den där känslan när man kommer in på hotellrummet för första gången och vet att man är långledig tillsammans hela helgen. Den känslan…<br><br><span class="tags">#långledig #välmående #momentofhappiness #solkvartsgillet #gillesliv</span></p>
    <div class="feed-media">
      <div class="photo" role="img" aria-label="Ljust hotellrum med bäddad säng och fönster" style="background:linear-gradient(180deg,#d9cfc2 0%,#c4b4a0 40%,#a58f76 60%,#eee9e2 78%,#8f7a64 100%)"></div>
      <div class="caption"><strong>Timeline Photos</strong><small>GLIMTORA.COM</small></div>
    </div>
  </div>
  <div class="share">Dela på <span class="c" style="background:var(--blue)"></span><span class="c" style="background:var(--red)"></span><span class="c" style="background:var(--blue)"></span><span class="c" style="background:var(--sky)"></span></div>
</section>

<!-- footer -->
<footer class="abs footer">
  <div class="col" style="left:99px;width:230px">
    <h4>ABOUT US</h4>
    <p>Lorem ipsum dolor sit amet, consectetur adipiscing elit, sed do eiusmod tempor incididunt ut labore et dolore magna aliqua. Ut enim ad minim veniam, quis nostrud exercitation ullamco laboris nisi ut aliquip ex ea commodo consequat.</p>
  </div>
  <div class="col" style="left:355px">
    <h4>QUICK LINKS</h4>
    <ul class="links"><li>Hem</li><li>Gillesresor</li><li>Inspiration</li><li>Medlemserbjudanden</li><li>Om</li><li>Inspiration</li></ul>
  </div>
  <div class="col" style="left:527px">
    <h4>FOLLOW US</h4>
    <div class="follow"><span></span><span></span><span></span><span></span><span></span><span></span></div>
  </div>
  <div class="col newsletter" style="left:700px;width:398px">
    <h4>NEWSLETTER SIGN UP</h4>
    <p>Lorem ipsum dolor sit amet, consectetur adipiscing elit, sed do eiusmod tempor incididunt ut labore et …</p>
    <form><input type="text" placeholder="Enter your email adress"><button type="button">SIGN UP</button></form>
  </div>
</footer>
<div class="abs copyright">© 2016 Solkvartsgillet. All Rights Reserved.</div>

</body>
</html>
```